Four in One (Flexible infographic for Content Management Industry)

See attachment.
A graphic depicting 4 products, where each can stand on its own and each can be combined with others, but where, if all are taken together, the best result is achieved (the "super product").
Intended use is web. See attached file as an example.
The most basic idea is as the attached diagram shows, where 4 rectangles are arranged in a quadrangle, with a middle rectangle in the center representing the combined 4 products. This concept is fine except it is a bit too obvious as it stands. We are looking for either a variation of this or another concept.
The audience is technical + professional + enterprise - NOT consumers. Hence the design should be conservative in nature.
We are aware of tools like as Canva or Pictogram where such graphics are available, but we are looking for something with a bit more imagination and flexibility.
This graphic should be targeted to web sites and be delivered with vector-based (SVG) graphics.

```html
<!DOCTYPE html>
<html lang="en">
<head>
<meta charset="utf-8">
<title>Four in One – Super Product</title>
<link href="https://fonts.googleapis.com/css2?family=Nunito:wght@600;700;800;900&display=swap" rel="stylesheet">
<style>
  :root {
    --navy: #4f6189;
    --navy-text: #3e4e74;
    --plum: #5e2d55;
    --plum-text: #6b2c5c;
    --magenta: #c21a7f;
    --teal: #52a8b0;
    --orange: #f28a33;
    --ink: #333333;
    --head-bg: #e6e7e9;
    --desc-bg: #f7f7f7;
    --list-bg: #ffffff;
    --page: #ffffff;
  }
  * { margin: 0; padding: 0; box-sizing: border-box; }
  html, body { width: 1200px; height: 713px; overflow: hidden; background: var(--page); }
  body { font-family: "Nunito", sans-serif; color: var(--ink); position: relative; }

  .pillar { position: absolute; top: 35px; width: 259px; height: 436px; }
  .pillar-cap { height: 7px; }
  .pillar-head { height: 153px; background: var(--head-bg); position: relative; border-bottom: 2px solid #2e2e2e; }
  .pillar-icon { position: absolute; left: 50%; top: 12px; transform: translateX(-50%); width: 62px; height: 62px; }
  .pillar-title { position: absolute; left: 0; right: 0; top: 88px; text-align: center; font-weight: 900; font-size: 25px; line-height: 25px; }
  .pillar-desc { height: 148px; background: var(--desc-bg); padding: 14px 14px 0; text-align: center; font-weight: 700; font-size: 14px; line-height: 18px; }
  .pillar-list { height: 113px; background: var(--list-bg); list-style: none; padding: 16px 0 0 18px; font-weight: 700; font-size: 11.5px; line-height: 14.5px; border: 1px solid #eeeeee; border-top: none; }
  .pillar-list li::before { content: "✔"; margin-right: 6px; }
  .pillar-foot { height: 16px; }

  .pillar--docs { left: 52px; }
  .pillar--docs .pillar-cap, .pillar--docs .pillar-foot { background: var(--navy); }
  .pillar--docs .pillar-title { color: var(--navy-text); top: 92px; }
  .pillar--docs .pillar-desc { font-weight: 600; font-size: 14px; line-height: 19.5px; }
  .pillar--docs .pillar-list { font-weight: 600; padding-left: 17px; }

  .pillar--security { left: 329px; }
  .pillar--security .pillar-cap, .pillar--security .pillar-foot { background: var(--plum); }
  .pillar--security .pillar-title { color: var(--plum-text); top: 86px; }
  .pillar--security .pillar-list { padding-left: 27px; }

  .pillar--digital { left: 613px; }
  .pillar--digital .pillar-cap, .pillar--digital .pillar-foot { background: var(--teal); }
  .pillar--digital .pillar-title { top: 86px; }
  .pillar--digital .pillar-list { padding-left: 6px; }

  .pillar--erp { left: 897px; }
  .pillar--erp .pillar-cap, .pillar--erp .pillar-foot { background: var(--orange); }
  .pillar--erp .pillar-title { top: 92px; left: 6px; right: -12px; white-space: nowrap; }
  .pillar--erp .pillar-desc { text-align: left; padding-left: 6px; }
  .pillar--erp .pillar-list { padding: 14px 0 0 15px; }

  .combine { position: absolute; left: 52px; top: 489px; width: 1103px; height: 188px; background: var(--head-bg); }
  .combine-edge { position: absolute; left: 0; width: 100%; height: 4px; display: flex; }
  .combine-edge span { flex: none; height: 100%; }
  .combine-edge--top { top: 0; }
  .combine-edge--bottom { bottom: 0; }
  .combine-title { position: absolute; left: 0; right: 0; top: 28px; text-align: center; font-weight: 900; font-size: 104px; line-height: 130px; letter-spacing: 1px; color: var(--ink); word-spacing: 12px; }

  .connectors { position: absolute; left: 0; top: 0; width: 1200px; height: 713px; pointer-events: none; }
</style>
</head>
<body>

  <section class="pillar pillar--docs">
    <div class="pillar-cap"></div>
    <header class="pillar-head">
      <svg class="pillar-icon" viewBox="0 0 62 62" aria-hidden="true">
        <circle cx="31" cy="31" r="29" fill="none" stroke="var(--navy)" stroke-width="2.5"/>
        <path d="M22 15h13l7 7v25H22z" fill="none" stroke="var(--navy)" stroke-width="2"/>
        <path d="M35 15v7h7" fill="none" stroke="var(--navy)" stroke-width="2"/>
        <path d="M26 27h12M26 31h12M26 35h12M26 39h12" stroke="var(--navy)" stroke-width="1.6"/>
      </svg>
      <h2 class="pillar-title">Document<br>Management</h2>
    </header>
    <p class="pillar-desc">Streamline document organization, access, and collaboration with easier file storage and sharing, leading to more efficient workflows .</p>
    <ul class="pillar-list">
      <li>Centralized Document Control</li>
      <li>Collaborative Workspace Integration</li>
      <li>Automated Compliance Tracking</li>
      <li>Check 4</li>
    </ul>
    <div class="pillar-foot"></div>
  </section>

  <section class="pillar pillar--security">
    <div class="pillar-cap"></div>
    <header class="pillar-head">
      <svg class="pillar-icon" viewBox="0 0 62 62" aria-hidden="true" style="top:6px">
        <path d="M31 4l-6 5-12 2v20c0 13 9 21 18 25 9-4 18-12 18-25V11l-12-2z" fill="none" stroke="var(--magenta)" stroke-width="4" stroke-linejoin="round"/>
        <path d="M22 31l7 7 12-14" fill="none" stroke="var(--magenta)" stroke-width="4.5" stroke-linecap="round" stroke-linejoin="round"/>
      </svg>
      <h2 class="pillar-title">Security<br>and Compliance</h2>
    </header>
    <p class="pillar-desc">Benefit from tailored cloud solutions, secure data storage, and expert disaster recovery planning for reliable and scalable IT operations.</p>
    <ul class="pillar-list">
      <li>Custom Cloud Solutions</li>
      <li>Secure Data Storage</li>
      <li>Expert Disaster Recovery</li>
      <li>Check 4</li>
    </ul>
    <div class="pillar-foot"></div>
  </section>

  <section class="pillar pillar--digital">
    <div class="pillar-cap"></div>
    <header class="pillar-head">
      <svg class="pillar-icon" viewBox="0 0 62 62" aria-hidden="true" style="top:6px">
        <path d="M3 22a40 40 0 0 1 56 0" fill="none" stroke="var(--teal)" stroke-width="3.5" stroke-linecap="round"/>
        <path d="M10 29a30 30 0 0 1 42 0" fill="none" stroke="var(--teal)" stroke-width="3.5" stroke-linecap="round"/>
        <path d="M17 36a20 20 0 0 1 28 0" fill="none" stroke="var(--teal)" stroke-width="3.5" stroke-linecap="round"/>
        <path d="M24 43a10 10 0 0 1 14 0" fill="none" stroke="var(--teal)" stroke-width="3.5" stroke-linecap="round"/>
        <circle cx="31" cy="51" r="5" fill="var(--teal)"/>
      </svg>
      <h2 class="pillar-title">Digital<br>Transformation</h2>
    </header>
    <p class="pillar-desc">Turn scanned documents into easily searchable digital archives, boosting efficiency and accessibility.</p>
    <ul class="pillar-list">
      <li>Instant searchable Archives with OCR</li>
      <li>Automated Document Classification</li>
      <li>ShareHub and Cloud Blob Ready</li>
      <li>Check 4</li>
    </ul>
    <div class="pillar-foot"></div>
  </section>

  <section class="pillar pillar--erp">
    <div class="pillar-cap"></div>
    <header class="pillar-head">
      <svg class="pillar-icon" viewBox="0 0 62 62" aria-hidden="true" style="top:14px">
        <rect x="22" y="8" width="30" height="50" fill="none" stroke="var(--orange)" stroke-width="3"/>
        <rect x="13" y="2" width="32" height="51" fill="var(--head-bg)" stroke="var(--orange)" stroke-width="3"/>
        <path d="M19 15h20M19 22h20M19 29h20M19 36h20M19 43h14" stroke="var(--orange)" stroke-width="3"/>
      </svg>
      <h2 class="pillar-title">Enterprise<br>Resource Planning</h2>
    </header>
    <p class="pillar-desc">Simplify management across finance, sales, and operations, enabling better decision-making and improved productivity.</p>
    <ul class="pillar-list">
      <li>Integrated Business Processes</li>
      <li>Enhanced Decision-Making</li>
      <li>Productivity Improvement</li>
      <li>Check 4</li>
    </ul>
    <div class="pillar-foot"></div>
  </section>

  <section class="combine">
    <div class="combine-edge combine-edge--top">
      <span style="width:276px;background:var(--navy)"></span>
      <span style="width:276px;background:var(--plum)"></span>
      <span style="width:275px;background:var(--teal)"></span>
      <span style="width:276px;background:var(--orange)"></span>
    </div>
    <h1 class="combine-title">Super Product</h1>
    <div class="combine-edge combine-edge--bottom">
      <span style="width:276px;background:var(--navy)"></span>
      <span style="width:276px;background:var(--plum)"></span>
      <span style="width:275px;background:var(--teal)"></span>
      <span style="width:276px;background:var(--orange)"></span>
    </div>
  </section>

  <svg class="connectors" viewBox="0 0 1200 713" aria-hidden="true">
    <path d="M167 470h28v22h14l-28 28-28-28h14z" fill="var(--navy)"/>
    <path d="M440 470h28v22h14l-28 28-28-28h14z" fill="var(--plum)"/>
    <path d="M728 470h28v22h14l-28 28-28-28h14z" fill="var(--teal)"/>
    <path d="M1011 470h28v22h14l-28 28-28-28h14z" fill="var(--orange)"/>
  </svg>

</body>
</html>
```